label design for cannabis

label template 4"x5.5" for a Massachusetts cannabis beverage product. labels will be transparent and placed on a blue (pantone 306C) bag.
https://www.drizzlepods.com/

Target Market(s)

cannabis customers in MA, 21+

Industry/Entity Type

cannabis consumer product

Font styles to use
Other font styles liked:
• DIN

Colors
0094D4
00A9DD
6FCCEA
C7EBF8
E9F6FB

Requirements
Must have
• label design with fizz logo, flavor (lemon, lime, plain, and coffee). 306C pantone for background and 11-0601 TCX for text. font=DINackground.
Nice to have
• tray icon, illustrated ice cubes in white (clear), yellow (lemon), green (lime) and brown (coffee)
Should not have
• no cartoonish characters

```html
<!DOCTYPE html>
<html lang="en">
<head>
<meta charset="utf-8">
<title>fizz infused ice cubes – clear label</title>
<link rel="stylesheet" href="https://fonts.googleapis.com/css2?family=Barlow+Condensed:wght@500;600&family=Barlow:wght@500;600;700&display=swap">
<style>
  :root {
    --navy: #1f3468;
    --navy-light: #2a4380;
    --white: #ffffff;
    --off-white: #f4f5f0;
  }
  * { margin: 0; padding: 0; box-sizing: border-box; }
  html, body {
    width: 873px;
    height: 1200px;
    overflow: hidden;
    background: var(--navy);
  }
  .label {
    position: relative;
    width: 873px;
    height: 1200px;
    background: var(--navy);
    color: var(--white);
    font-family: "Barlow", sans-serif;
  }
  .label__frame {
    position: absolute;
    left: 38px;
    top: 34px;
    width: 797px;
    height: 1132px;
    border: 4px solid var(--white);
    border-radius: 44px;
  }
  .brand {
    position: absolute;
    left: 0;
    width: 100%;
    top: 96px;
    text-align: center;
    font-family: "Barlow Condensed", sans-serif;
    font-weight: 600;
    font-size: 250px;
    line-height: 1;
    letter-spacing: -4px;
  }
  .tagline {
    position: absolute;
    left: 0;
    width: 100%;
    top: 324px;
    text-align: center;
    font-family: "Barlow Condensed", sans-serif;
    font-weight: 600;
    font-size: 72px;
    line-height: 1;
    letter-spacing: -1px;
    transform: scaleX(0.86);
    transform-origin: 50% 0;
  }
  .cubes-art {
    position: absolute;
    left: 282px;
    top: 431px;
    width: 313px;
    height: 302px;
    border-radius: 24px;
    background: radial-gradient(circle at 50% 45%, var(--navy-light), var(--navy) 75%);
  }
  .flavor__rule {
    position: absolute;
    left: 338px;
    top: 782px;
    width: 197px;
    height: 3px;
    background: var(--white);
  }
  .flavor {
    position: absolute;
    left: 0;
    width: 100%;
    top: 794px;
    text-align: center;
    font-weight: 700;
    font-size: 52px;
    line-height: 1;
    letter-spacing: 2px;
  }
  .tray {
    position: absolute;
    left: 89px;
    top: 979px;
    width: 322px;
    height: 90px;
  }
  .tray__dose {
    position: absolute;
    left: 0;
    top: 0;
    width: 322px;
    height: 40px;
    line-height: 38px;
    text-align: center;
    font-weight: 500;
    font-size: 22px;
    letter-spacing: 0.5px;
  }
  .tray svg { position: absolute; left: 0; top: 0; }
  .age-badge {
    position: absolute;
    left: 656px;
    top: 950px;
    width: 142px;
    height: 142px;
    border: 6px solid var(--off-white);
    border-radius: 50%;
    text-align: center;
    color: var(--off-white);
  }
  .age-badge__caption {
    display: block;
    margin-top: 26px;
    font-family: "Barlow Condensed", sans-serif;
    font-weight: 600;
    font-size: 25px;
    line-height: 1;
  }
  .age-badge__number {
    display: block;
    font-weight: 700;
    font-size: 56px;
    line-height: 1;
    margin-top: -2px;
  }
  .website {
    position: absolute;
    left: 0;
    width: 100%;
    top: 1126px;
    text-align: center;
    font-weight: 500;
    font-size: 16px;
    letter-spacing: 0.5px;
  }
</style>
</head>
<body>
  <main class="label">
    <div class="label__frame"></div>

    <h1 class="brand">fizz</h1>
    <p class="tagline">infused ice cubes</p>

    <div class="cubes-art" role="img" aria-label="Illustration of three white outlined ice cubes"></div>

    <div class="flavor__rule"></div>
    <p class="flavor">clear</p>

    <div class="tray">
      <svg width="322" height="90" viewBox="0 0 322 90" aria-hidden="true">
        <g fill="none" stroke="#ffffff" stroke-width="3.5" stroke-linejoin="miter">
          <rect x="1.75" y="1.75" width="318.5" height="38"/>
          <path d="M11 40 L17 88 L62 88 L67 40"/>
          <path d="M72 40 L78 88 L123 88 L128 40"/>
          <path d="M133 40 L139 88 L185 88 L190 40"/>
          <path d="M195 40 L201 88 L247 88 L252 40"/>
          <path d="M257 40 L263 88 L309 88 L314 40"/>
        </g>
      </svg>
      <p class="tray__dose">50 mg per cube</p>
    </div>

    <div class="age-badge">
      <span class="age-badge__caption">FOR AGE</span>
      <span class="age-badge__number">21+</span>
    </div>

    <p class="website">www.drizzlepods.com</p>
  </main>
</body>
</html>
```